Business Cards

Business cards (double-sided) to be handed out to clients and potential clients, with contact details, logo .

Target Market(s)

Small to medium size businesses

Industry/Entity Type

Accountants

Contact Information for Business Card

Brightwater Ledger & Counsel Ltd

Colors

Designer to choose only greyscale colors for use in the design.

Requirements
Must have
• Name, Title, Address, Phone number, Email, Website
Nice to have
• Modern, clean lines, classy
Should not have
• Business cards to be double-sided. Form keeps reverting to single-sided.

```html
<!DOCTYPE html>
<html lang="en">
<head>
<meta charset="utf-8">
<title>Brightwater Ledger &amp; Counsel – Business Card</title>
<link rel="stylesheet" href="https://fonts.googleapis.com/css2?family=Josefin+Sans:wght@400;600&family=Roboto+Condensed:wght@300;400&display=swap">
<style>
  :root {
    --page: #2b2b2d;
    --card-light: #ffffff;
    --card-dark: #111112;
    --ink: #141414;
    --ink-soft: #6e6e6e;
    --rule-dark: #575757;
    --paper-text: #ffffff;
  }
  * { box-sizing: border-box; margin: 0; padding: 0; }
  html, body {
    width: 1200px; height: 960px; overflow: hidden;
    background: var(--page);
  }
  .sheet {
    width: 1200px; height: 960px;
    display: flex; flex-direction: column;
    align-items: center; justify-content: center; gap: 60px;
  }
  .card {
    position: relative;
    width: 700px; height: 400px;
    border-radius: 4px;
    box-shadow: 0 18px 40px rgba(0,0,0,.45);
    overflow: hidden;
  }
  .card--back { background: var(--card-dark); }
  .card--front { background: var(--card-light); color: var(--ink); }

  .rules { position: absolute; inset: 0; }
  .rules line { stroke: var(--rule-dark); stroke-width: 1; }

  .wordmark {
    font-family: "Josefin Sans", sans-serif;
    font-weight: 400;
    text-transform: uppercase;
    letter-spacing: .16em;
    line-height: 1.3;
    display: flex; align-items: center; gap: 14px;
    white-space: nowrap;
  }
  .wordmark__square { width: 12px; height: 12px; flex: none; }
  .card--back .wordmark {
    position: absolute; left: 50%; top: 50%;
    transform: translate(-50%, -50%);
    color: var(--paper-text); font-size: 28px;
  }
  .card--back .wordmark__square { border: 1.5px solid var(--paper-text); }

  .card--front .wordmark {
    position: absolute; left: 44px; top: 56px;
    font-size: 22px; color: var(--ink);
  }
  .card--front .wordmark__square { border: 1.5px solid var(--ink); }

  .holder {
    position: absolute; left: 372px; top: 140px;
  }
  .holder__name {
    font-family: "Josefin Sans", sans-serif; font-weight: 600;
    font-size: 25px; letter-spacing: .14em; text-transform: uppercase;
    white-space: nowrap;
  }
  .holder__title {
    font-family: "Roboto Condensed", sans-serif; font-weight: 300;
    font-size: 14px; color: var(--ink-soft); margin-top: 2px;
  }
  .contacts {
    list-style: none; margin-top: 12px;
    font-family: "Roboto Condensed", sans-serif; font-weight: 300;
    font-size: 16px; color: var(--ink-soft);
  }
  .contacts li { display: flex; align-items: center; gap: 12px; height: 25px; white-space: nowrap; }
  .contacts .web { color: var(--ink); }
  .icon { width: 16px; height: 16px; flex: none; fill: var(--ink); }

  .divider {
    position: absolute; left: 300px; right: 0; top: 296px;
    height: 1.5px; background: var(--ink);
  }
  .address {
    position: absolute; left: 300px; top: 314px;
    display: flex; gap: 12px;
    font-family: "Roboto Condensed", sans-serif; font-weight: 300;
    font-size: 17px; line-height: 1.35; color: var(--ink-soft);
    font-style: normal; white-space: nowrap;
  }
  .address .icon { margin-top: 2px; }
</style>
</head>
<body>
<main class="sheet">
  <section class="card card--back" aria-label="Card reverse">
    <svg class="rules" width="700" height="400" viewBox="0 0 700 400" aria-hidden="true">
      <line x1="80" y1="36" x2="80" y2="80"/>
      <line x1="80" y1="36" x2="664" y2="36"/>
      <line x1="620" y1="364" x2="620" y2="320"/>
      <line x1="36" y1="364" x2="620" y2="364"/>
      <line x1="430" y1="116" x2="650" y2="116"/>
      <line x1="50" y1="284" x2="270" y2="284"/>
    </svg>
    <div class="wordmark">
      <span class="wordmark__square"></span>
      <span>Brightwater<br>Ledger &amp;<br>Counsel</span>
    </div>
  </section>

  <section class="card card--front" aria-label="Card front">
    <div class="wordmark">
      <span class="wordmark__square"></span>
      <span>Brightwater<br>Ledger &amp;<br>Counsel</span>
    </div>

    <div class="holder">
      <h1 class="holder__name">Daniel Reyes</h1>
      <p class="holder__title">Owner</p>
      <ul class="contacts">
        <li>
          <svg class="icon" viewBox="0 0 24 24" aria-hidden="true"><path d="M6.6 10.8a15 15 0 0 0 6.6 6.6l2.2-2.2c.3-.3.7-.4 1-.2 1.1.4 2.3.6 3.6.6.6 0 1 .4 1 1V20c0 .6-.4 1-1 1A17 17 0 0 1 3 4c0-.6.4-1 1-1h3.5c.6 0 1 .4 1 1 0 1.3.2 2.5.6 3.6.1.3 0 .7-.2 1z"/></svg>
          <span>555-014-2873</span>
        </li>
        <li>
          <svg class="icon" viewBox="0 0 24 24" aria-hidden="true"><path d="M2 5h20v14H2zm2 2v.5l8 5 8-5V7zm0 2.8V17h16V9.8l-8 5z"/></svg>
          <span>info@brightwaterledger.com</span>
        </li>
        <li>
          <svg class="icon" viewBox="0 0 24 24" aria-hidden="true"><path d="M12 2a10 10 0 1 0 0 20 10 10 0 0 0 0-20zm6.9 9h-3a15 15 0 0 0-1.3-5.9A8 8 0 0 1 18.9 11zM12 4c.9 1.2 1.8 3.5 1.9 7h-3.8c.1-3.5 1-5.8 1.9-7zM9.4 5.1A15 15 0 0 0 8.1 11h-3a8 8 0 0 1 4.3-5.9zM5.1 13h3a15 15 0 0 0 1.3 5.9A8 8 0 0 1 5.1 13zm6.9 7c-.9-1.2-1.8-3.5-1.9-7h3.8c-.1 3.5-1 5.8-1.9 7zm2.6-1.1a15 15 0 0 0 1.3-5.9h3a8 8 0 0 1-4.3 5.9z"/></svg>
          <span class="web">www.brightwaterledger.com</span>
        </li>
      </ul>
    </div>

    <div class="divider" aria-hidden="true"></div>

    <address class="address">
      <svg class="icon" viewBox="0 0 24 24" aria-hidden="true"><path d="M12 2a7 7 0 0 0-7 7c0 5 7 13 7 13s7-8 7-13a7 7 0 0 0-7-7zm0 9.5a2.5 2.5 0 1 1 0-5 2.5 2.5 0 0 1 0 5z"/></svg>
      <span>418 Linden Ave, Suite 12<br>Fairhaven, MA 00000</span>
    </address>
  </section>
</main>
</body>
</html>
```